Brackenford Guard Service Business Card Design

Hi All

We have decided to update this project from the Meridale Protection and Patrol Outfitters to the one mentioned above.

We are a company that supplies guard services .
Updates

Project Deadline Extended
Reason: Since we have changed the projet to a new design and idea this gives veryone more time. we are all busy regards colin

please include the following details on the card

 Master License 536918407 or M/L 536918407

phone 02 7163 2987

the logo can be removed from the shield , ie scales and eagle with the writing    etc

thank you                       

Hi All

There are great design that have come in so far and thank you for your time and design.

Please adjust the design to include

Company Name

Name  - Colin Parsnow

Address - PO Box 358 Elmcrest 2061

Master License Number - 536 918 407

ABN - 62417 390518 

Web address  www.brackenfordguardservice.com.au

email -  security@brackenfordguardservice.com.au

Thank you

Colin

                                   

Target Market(s)

Commercial, Residential, Business, Government, Corporate

Industry/Entity Type

Business

Contact Information for Business Card

Colin Parsnow
General Manager 0438 725 914
ABN 62 417 390 518 0271632987
PO Box 358
Elmcrest 2061

www.brackenfordguardservice.com.au

Requirements
Must have
• the company logo as per attachment below

```html
<!DOCTYPE html>
<html lang="en">
<head>
<meta charset="utf-8">
<title>Brackenford Guard Service — Business Card</title>
<link href="https://fonts.googleapis.com/css2?family=Open+Sans:wght@400;700&family=Cinzel:wght@400&display=swap" rel="stylesheet">
<style>
  :root {
    --bg: #4a3f3a;
    --card: #1c1c1d;
    --card-edge: #111112;
    --gold: #f2c318;
    --gold-deep: #b88f0c;
    --text: #c9c9c9;
    --muted: #9a9a9a;
    --white: #ffffff;
    --silver: #8e8e8e;
  }
  * { box-sizing: border-box; margin: 0; padding: 0; }
  html, body { width: 1200px; height: 889px; overflow: hidden; }
  body {
    background: var(--bg);
    font-family: "Open Sans", Arial, sans-serif;
    position: relative;
  }
  .card {
    position: absolute;
    top: 290px;
    width: 540px;
    height: 309px;
    background: var(--card);
    border: 1px solid var(--card-edge);
    box-shadow: 0 10px 24px rgba(0,0,0,.45);
  }
  .card--back { left: 40px; }
  .card--front { left: 620px; }

  /* Back */
  .back-brand {
    position: absolute;
    top: 70px; left: 0; right: 0;
    text-align: center;
    color: var(--silver);
    font-weight: 700;
    font-size: 24px;
    line-height: 1.25;
    text-transform: uppercase;
  }
  .back-web {
    position: absolute;
    left: 40px; right: 40px; top: 210px;
    text-align: center;
    font-family: "Cinzel", Georgia, serif;
    font-size: 19px;
    letter-spacing: .5px;
    color: var(--silver);
  }
  .back-rule {
    position: absolute;
    left: 40px; right: 40px; top: 246px;
    height: 2px;
    background: linear-gradient(90deg, transparent, var(--gold) 40%, var(--gold-deep) 80%, transparent);
  }

  /* Front */
  .front-brand {
    position: absolute;
    left: 26px; top: 92px;
    width: 180px;
    text-align: center;
    color: var(--white);
    font-weight: 700;
    font-size: 21px;
    line-height: 1.3;
    text-transform: uppercase;
  }
  .divider {
    position: absolute;
    left: 222px; top: 40px;
    width: 1px; height: 130px;
    background: linear-gradient(var(--gold-deep), transparent);
  }
  .details {
    position: absolute;
    left: 240px; top: 34px; right: 16px;
    color: var(--text);
    font-size: 13px;
    line-height: 1.45;
  }
  .person-name { color: var(--gold); font-weight: 700; font-size: 22px; line-height: 1.1; }
  .person-role { color: var(--muted); font-size: 12.5px; margin-bottom: 14px; }
  .address { margin-bottom: 14px; }
  .contact-list { list-style: none; }
  .contact-list li { display: flex; align-items: center; gap: 7px; white-space: nowrap; }
  .contact-list svg { width: 10px; height: 10px; fill: var(--gold); flex: none; }
  .registrations {
    position: absolute;
    left: 26px; bottom: 22px;
    color: var(--gold);
    font-size: 13px;
    line-height: 1.45;
  }
</style>
</head>
<body>

  <section class="card card--back" aria-label="Card back">
    <div class="back-brand">Brackenford<br>Guard Service</div>
    <div class="back-web">WWW.BRACKENFORDGUARDSERVICE.COM.AU</div>
    <div class="back-rule"></div>
  </section>

  <section class="card card--front" aria-label="Card front">
    <div class="front-brand">Brackenford<br>Guard<br>Service</div>
    <div class="divider"></div>
    <div class="details">
      <div class="person-name">Colin Parsnow</div>
      <div class="person-role">General Manager</div>
      <div class="address">PO Box 358 Elmcrest 2061</div>
      <ul class="contact-list">
        <li><svg viewBox="0 0 10 10"><rect x="2.5" y="0" width="5" height="10" rx="1"/></svg>0438 725 914</li>
        <li><svg viewBox="0 0 10 10"><path d="M2 0h2l1 3-1.5 1a6 6 0 0 0 2.5 2.5L7 5l3 1v2c0 1-1 2-2 2C4 10 0 6 0 2c0-1 1-2 2-2z"/></svg>02 7163 2987</li>
        <li><svg viewBox="0 0 10 10"><path d="M0 2h10v6H0z M0 2l5 3.5L10 2" /></svg>security@brackenfordguardservice.com.au</li>
        <li><svg viewBox="0 0 10 10"><circle cx="5" cy="5" r="5"/></svg>www.brackenfordguardservice.com.au</li>
      </ul>
    </div>
    <div class="registrations">
      <div>ABN:&nbsp; 62 417 390 518</div>
      <div>Master License Number: 536 918 407</div>
    </div>
  </section>

</body>
</html>
```